Upscale business cards needed for Board of Directors

We need professional business cards created for members of our family business Board of Directors. We would like these relatively simple and straightforward, but also with a unique element to set them apart. Probably stick with neutral and simple colors - white, grey etc. We need space for the traditional elements, including name, title, address, email/phone number. And we will be creating several from this template so it needs to be template that is easy to switch information in and out of.
Business
See description

```html
<!DOCTYPE html>
<html lang="en">
<head>
<meta charset="utf-8">
<title>Board of Directors Business Card</title>
<link rel="stylesheet" href="https://fonts.googleapis.com/css2?family=Montserrat:wght@500;600&display=swap">
<style>
  :root {
    --backdrop: #2a2725;
    --card-white: #ffffff;
    --tan-light: #d8c9a6;
    --tan-dark: #a48f66;
    --gold: #c2a36a;
    --gold-ring: #8a6d3b;
    --ink: #1e1c1a;
    --name-white: #ffffff;
  }
  * { margin: 0; padding: 0; box-sizing: border-box; }
  html, body {
    width: 1200px; height: 1200px; overflow: hidden;
    background: var(--backdrop);
  }
  .canvas {
    position: relative; width: 1200px; height: 1200px;
    display: flex; align-items: center; justify-content: center;
  }
  .business-card {
    position: relative; width: 1000px; height: 572px;
    background: var(--card-white);
    overflow: hidden;
    box-shadow: 0 18px 40px rgba(0,0,0,0.45);
    font-family: "Montserrat", sans-serif;
  }
  .tan-field { position: absolute; inset: 0; }
  .brand-disc {
    position: absolute; left: 640px; top: 70px;
    width: 340px; height: 340px; border-radius: 50%;
    background: var(--card-white);
    border: 4px solid var(--gold-ring);
    display: flex; flex-direction: column;
    align-items: center; justify-content: center;
  }
  .brand-name {
    color: var(--ink); font-weight: 600;
    font-size: 34px; letter-spacing: 2px; line-height: 1.25;
    text-align: center; text-transform: uppercase;
  }
  .holder {
    position: absolute; left: 90px; top: 250px;
  }
  .holder-name {
    color: var(--name-white); font-weight: 500;
    font-size: 38px; letter-spacing: 2px; text-transform: uppercase;
  }
  .holder-title {
    color: var(--ink); font-weight: 500;
    font-size: 27px; letter-spacing: 1.5px; text-transform: uppercase;
    margin-top: 4px;
  }
  .contact-list {
    position: absolute; left: 90px; top: 390px;
    list-style: none;
    color: var(--ink); font-weight: 500; font-size: 24px; line-height: 38px;
  }
  .contact-list li { display: flex; }
  .contact-label { color: var(--gold); width: 48px; flex: none; }
</style>
</head>
<body>
<main class="canvas">
  <article class="business-card">
    <svg class="tan-field" width="1000" height="572" viewBox="0 0 1000 572" aria-hidden="true">
      <defs>
        <linearGradient id="tanGradient" x1="0" y1="0" x2="1" y2="0.4">
          <stop offset="0" stop-color="var(--tan-light)" style="stop-color:#d8c9a6"/>
          <stop offset="1" stop-color="var(--tan-dark)" style="stop-color:#a48f66"/>
        </linearGradient>
      </defs>
      <polygon points="0,0 1000,0 1000,250 0,370" fill="url(#tanGradient)"/>
    </svg>

    <div class="brand-disc">
      <span class="brand-name">Harbourline<br>Holdings</span>
    </div>

    <header class="holder">
      <h1 class="holder-name">Viverra Quam</h1>
      <p class="holder-title">Lorem Ipsum</p>
    </header>

    <ul class="contact-list">
      <li><span class="contact-label">M:</span><span>+44 000 000 0000</span></li>
      <li><span class="contact-label">E:</span><span>loremipsum@hl-board.com</span></li>
      <li><span class="contact-label">A:</span><span>consectetur adipiscing elit. Phasellus quis orci imperdiet,<br>blandit sapien et, condimentum odio</span></li>
    </ul>
  </article>
</main>
</body>
</html>
```